Saving Lives with Dental Sleep Medicine

Looking for a brochure to market Dental Sleep Medicine educational courses . Whoever wins this bid will be hired to design the rest of our marketing campaign.
Design should be clean, simple with a modern feel. Not busy. Our courses utilize the most modern technology available.
Brochure content is attached, if you can't fit it all that is ok, we can tweak the content later. We are more focused on the look and feel of this design.
This brochure is marketing a 2 day course so there needs to be a spot for date, location, time & cost. As well as a notice of where to register VelmoraLearning.com, info@velmoralearning.com or call 1.800.###.#### and registration fees.
Also need a spot for Dr. Pelloquist's bio (attached). It's too long so just leave as much space as you can and we can amend the content.
Thank you so much. Looking forward to your designs. VelmEd Team :-)
Updates
Hello,
We are hoping for a minimalist design. Not busy. Clean and simple. We can reduce and minimize verbiage as needed. Just looking for layout and design.
Target Market(s)
Dentists
Requirements
Must have
- Clean lines, simple feel, minimalist and modern. Same font as logo. Black, white, gray.
Should not have
- Busy look and feel

```html
<!DOCTYPE html>
<html lang="en">
<head>
<meta charset="utf-8">
<title>Sleep &amp; Airway Management in a Dental Clinic – Course Flyer</title>
<link rel="stylesheet" href="https://fonts.googleapis.com/css2?family=Lato:wght@300;400;700;900&family=Oswald:wght@600;700&display=swap">
<style>
:root{
  --pink:#ef6b78;
  --pink-dark:#d95868;
  --grey-band:#a3a3ab;
  --grey-panel:#e8e8ea;
  --grey-text:#8d8d96;
  --ink:#1f1f22;
  --white:#ffffff;
  --backdrop:#f1f1f3;
}
*{box-sizing:border-box;margin:0;padding:0}
html,body{width:1200px;height:997px;overflow:hidden;background:var(--backdrop)}
body{font-family:"Lato",sans-serif;color:var(--ink);position:relative}
.page{position:absolute;top:126px;width:525px;height:744px;background:var(--white);overflow:hidden;box-shadow:0 4px 14px rgba(0,0,0,.18)}
.page--front{left:64px}
.page--back{left:611px}

.header{position:absolute;left:0;top:0;width:100%;height:80px;background:var(--pink)}
.brand{position:absolute;left:28px;top:24px;color:var(--white);font:300 27px/1 "Lato",sans-serif;letter-spacing:.3px}
.header__url{position:absolute;right:20px;top:36px;color:var(--white);font:700 12px/1 "Lato",sans-serif}
.call-tab{position:absolute;right:0;top:56px;width:250px;height:36px;background:var(--grey-band);clip-path:polygon(22px 0,100% 0,100% 100%,0 100%);color:var(--white);font:700 16px/36px "Lato",sans-serif;text-align:right;padding-right:20px}
.call-tab::before{content:"";position:absolute}
.fold{position:absolute;right:238px;top:86px;width:14px;height:8px;background:#6f6f76;clip-path:polygon(0 0,100% 0,100% 100%)}

.side-panel{position:absolute;left:0;top:120px;width:242px;height:554px;background:var(--grey-panel);border-top-right-radius:28px}
.tag{position:absolute;left:0;top:160px;width:216px;height:40px;background:var(--pink);color:var(--white);font:700 16px/40px "Lato",sans-serif;text-align:center;box-shadow:6px 6px 0 #b9b9bf}
.checklist{position:absolute;left:15px;list-style:none;font-size:9.6px;line-height:12.8px}
.checklist li{position:relative;padding-left:17px}
.checklist li::before{content:"";position:absolute;left:1px;top:2px;width:8px;height:8px;border:1px solid var(--ink);border-radius:50%}
.checklist li::after{content:"";position:absolute;left:4px;top:3px;width:3px;height:5px;border:solid var(--ink);border-width:0 1.3px 1.3px 0;transform:rotate(40deg)}
.topics{top:232px;width:222px}
.objectives{top:230px;width:220px;font-size:10px;line-height:12.8px}

.divider-gap{position:absolute;left:0;top:494px;width:242px;height:4px;background:var(--white)}
.course-desc{position:absolute;left:16px;top:518px;width:212px}
.course-desc h2{font:900 17px/1 "Lato",sans-serif;margin-bottom:8px}
.course-desc p{font-size:7.6px;line-height:10.6px;text-align:justify}

.title{position:absolute;left:262px;top:118px;width:248px;text-align:right;color:var(--pink);font:700 28px/32px "Oswald",sans-serif;text-transform:uppercase;letter-spacing:.3px}
.subtitle{position:absolute;left:262px;top:222px;width:248px;text-align:right;color:var(--grey-text);font:400 18px/23px "Lato",sans-serif}
.photo-circle{position:absolute;border-radius:50%;border:3px solid var(--pink)}
.photo-circle--class{left:274px;top:294px;width:232px;height:232px;background:radial-gradient(circle at 50% 45%,#9c948c,#5a5652 60%,#3b3a3c)}
.photo-circle--portrait{left:296px;top:120px;width:172px;height:172px;background:radial-gradient(circle at 50% 40%,#d9d9d9,#8a8a8a 60%,#3c3c3c)}
.program-text{position:absolute;left:275px;top:548px;width:235px;color:var(--grey-text);font-size:7.6px;line-height:10.6px;text-align:justify}

.footer{position:absolute;left:0;top:674px;width:100%;height:70px;background:var(--pink);color:var(--white)}
.footer__cell{position:absolute;top:19px;font-size:12.5px;line-height:16px}
.footer__cell b{font-weight:700}
.footer__rule{position:absolute;top:12px;width:2px;height:46px;background:var(--white)}
.cell-date{left:40px}
.cell-address{left:184px;width:200px}
.cell-cost{left:402px}

.bio{position:absolute;left:262px;top:316px;width:246px;color:var(--grey-text);font-size:7.2px;line-height:9.6px;text-align:justify}
.bio p{margin-bottom:9px}
.bio strong{color:#6d6d74;font-style:italic;font-size:9px}
.photo-rect{position:absolute;left:18px;width:206px;height:90px}
.photo-rect--seminar{top:475px;background:linear-gradient(110deg,#4a4644,#8d8580 50%,#cfc8c0)}
.photo-rect--scan{top:578px;background:linear-gradient(100deg,#6e6864,#2f3b52 55%,#b8bcc4)}

.contact{position:absolute;left:0;top:14px;width:100%;text-align:center}
.contact__head{display:flex;align-items:center;justify-content:center;gap:8px;font-size:13px}
.contact__head::before,.contact__head::after{content:"";width:124px;height:1.5px;background:var(--white)}
.contact__line{font:700 12.6px/1 "Lato",sans-serif;margin-top:6px}
</style>
</head>
<body>

<section class="page page--front">
  <header class="header">
    <div class="brand">VelmoraLearning</div>
    <div class="header__url">www.VelmoraLearning.com</div>
  </header>
  <div class="call-tab">Call: 1.800.###.####</div>

  <div class="side-panel"></div>
  <div class="tag">TOPICS COVERED:</div>
  <ul class="checklist topics">
    <li>Fundamentals of Sleep &amp; Sleep Disorders</li>
    <li>Understand Obstructive Sleep Apnea (OSA) &amp; Treatment Options</li>
    <li>How to Implement an effective Sleep Screening Protocol in a Dental Clinic</li>
    <li>Sleep Testing</li>
    <li>How to order an appliance for OAT</li>
    <li>Appliance Selection</li>
    <li>Importance of patient selection</li>
    <li>Overview of NOVIRA Plus System</li>
    <li>Hands-on workshop for NOVIRA Tray Fitting</li>
    <li>Hands-on workshop for Bite-Registration</li>
    <li>Technology &amp; Sleep</li>
    <li>Fully Digital Workflow for OAT</li>
    <li>NOVIRA Plus Case Studies</li>
    <li>Medical Billing for OAT</li>
    <li>How to maximize the utilization of your NOVIRA Plus at your clinic</li>
    <li>Simple and easy to follow clinical workflow</li>
  </ul>
  <div class="divider-gap"></div>
  <div class="course-desc">
    <h2>COURSE DESCRIPTION:</h2>
    <p>Dental Sleep Medicine (DSM) has been growing rapidly over the past decade. Despite such growth, Oral Appliance Therapy (OAT) could be challenging in terms of predictability and workflow efficiency, resulting in many clinicians being reluctant to incorporate “Sleep &amp; OAT” into their clinics. However, most of these challenges can now be addressed by utilizing available technologies in healthcare industry; resulting in improved and predictable clinical workflows, patient experience, quality of care and access to care.</p>
  </div>

  <h1 class="title">Sleep &amp; Airway Management in a Dental Clinic</h1>
  <p class="subtitle">NOVIRA Plus System &amp; Fully Digital Workflows for OAT</p>
  <div class="photo-circle photo-circle--class" role="img" aria-label="Photo of a hands-on workshop with dentists gathered around a dental chair"></div>
  <p class="program-text">This program will review the importance of Sleep &amp; Airway Management in comprehensive inter-disciplinary treatment planning and how airway &amp; sleep disorders, if left untreated, could adversely impact the long-term prognosis of dental treatments. It will also provide a practical step-by-step guide for implementing a simple &amp; predictable “Sleep and Airway Management” program; utilizing easy to implement systems, improved patient communication &amp; education through Intraoral scanning, &amp; 3D imaging AND a fully digital workflow for OAT.</p>

  <footer class="footer">
    <div class="footer__cell cell-date"><b>Date:</b> 01 01 19<br><b>Time:</b> 2 pm to 4 pm</div>
    <div class="footer__rule" style="left:166px"></div>
    <div class="footer__cell cell-address"><b>Address:</b> Lorem ipsum dolor sit amet, consectetuer adipisc</div>
    <div class="footer__rule" style="left:379px"></div>
    <div class="footer__cell cell-cost">Cost Par Head<br><b>$ 00.00</b></div>
  </footer>
</section>

<section class="page page--back">
  <header class="header">
    <div class="brand">VelmoraLearning</div>
    <div class="header__url">www.VelmoraLearning.com</div>
  </header>
  <div class="call-tab">Call: 1.800.###.####</div>

  <div class="side-panel"></div>
  <div class="tag">LEARNING OBJECTIVES:</div>
  <ul class="checklist objectives">
    <li>Step by step instruction on how to systematically integrate sleep into your practice</li>
    <li>Why dental clinics should have a comprehensive understanding of sleep &amp; airway disorders, and educate their patients</li>
    <li>How to implement a sleep and airway management program in a dental clinic</li>
    <li>Overview of some of the latest technologies in dentistry and how each could be utilized in Dental Sleep Medicine (DSM)</li>
    <li>How to utilize your NOVIRA Plus System effectively in your clinic</li>
    <li>Proper selection of oral appliances for OSA</li>
    <li>Medical Billing for OAT</li>
  </ul>
  <div class="photo-rect photo-rect--seminar" role="img" aria-label="Photo of the instructor presenting to a seated group"></div>
  <div class="photo-rect photo-rect--scan" role="img" aria-label="Photo of a clinician reviewing a 3D airway scan on a monitor"></div>

  <div class="photo-circle photo-circle--portrait" role="img" aria-label="Portrait of the course instructor"></div>
  <div class="bio">
    <p><strong>Dr. Pelloquist</strong> received his Doctor of Dental Surgery (DDS) Degree and Bachelor of Medical Sciences from Northvale University. He also earned fellowships from the Institute of Occlusal Physiology &amp; the Harbor Institute for Advanced Dental Studies. He then furthered his education and training by completing a Research Fellowship in the area of “Sleep and Dental Sleep Medicine” at Ridgeford University Hospital (RUH).</p>
    <p>Dr. Pelloquist is a general dentist who maintains a group of private practices with an interest in Dental Sleep Medicine and TMD Management. He is actively involved in clinical research in Dental Sleep Medicine and his research focuses on developing new technologies to improve treatment outcome predictability and patient selection in Oral Appliance Therapy for patients with OSA (i.e. Obstructive Sleep Apnea) and improving clinical workflow efficiencies, utilizing different digital technologies. He is the recipient of the “2012 &amp; 2015 Clinical Research Award” and “2015 Clinical Excellence Award” from the Academy of Oral Sleep Care (AOSC). He has lectured at numerous meetings and sleep conferences across North America and Europe.</p>
    <p>He is the founder and director of the Prairie Dental Sleep Study Club and the Clinical Director at The Quiet Night Centre. He is also the Chief Dental Officer at Halden Sleep Technologies, the developer of “NOVIRA TM” Technology. Dr. Pelloquist is a major advocate for the importance of an inter-disciplinary approach to Dental Sleep Medicine which focuses on the collaboration of Sleep Physicians, Sleep Dentists and other healthcare professionals. He has been treating OSA patients for many years and also has trained hundreds of dentists in Dental Sleep Medicine.</p>
  </div>

  <footer class="footer">
    <div class="contact">
      <div class="contact__head">Contact us For Registration</div>
      <div class="contact__line">VelmoraLearning.com | info@velmoralearning.com | Call: 1.800.###.####</div>
    </div>
  </footer>
</section>

</body>
</html>
```